Brand design for Corvanel Holdings

We are a new start up Fund Manager based in Singapore in need of a stylish and slick corporate identity starting with letterhead and business card (2 separate projects on pixel bazaar but must be completed as one). We are aiming to be a somewhat 'budget' service provider with a target market of high net worth individuals and savvy self traders so we need to have our look convey value but with style. Our logo is attached and the use of the blue is imperative. The company name is Corvanel Holdings Pte Ltd and the verbiage 'Licensed by the Treasury Conduct Bureau of Singapore - QTLD licence no. XQZ908172-3' should be incorporated in small print.

Business card should also include address, office, direct and mobile numbers as well as email address. Follow me on blabber/pk/workloop/Zentro+ should also be incrorporated. We are also looking to have a QR code on the business card that people can read with a smartphone which will auto populate our contact details in to their address book.

Many thanks and happy designing!

Reason: Extending so we can have further internal discussions. Thanks for input so far, some great designs coming through! Cheers

```html
<!DOCTYPE html>
<html lang="en">
<head>
<meta charset="utf-8">
<title>Corvanel Holdings — Letterhead</title>
<link rel="stylesheet" href="https://fonts.googleapis.com/css2?family=Mulish:wght@400;700;800&display=swap">
<style>
  :root {
    --backdrop: #d9d9d9;
    --paper: #ffffff;
    --brand-blue: #2b4f9c;
    --brand-blue-deep: #1f4390;
    --brand-blue-light: #3f8dc6;
    --band-grey: #7c808e;
    --text-grey: #5d5f66;
  }
  * { margin: 0; padding: 0; box-sizing: border-box; }
  html, body {
    width: 1200px; height: 968px; overflow: hidden;
    background: var(--backdrop);
    font-family: "Mulish", Arial, sans-serif;
  }
  .letterhead {
    position: absolute;
    left: 280px; top: 31px;
    width: 640px; height: 906px;
    background: var(--paper);
    box-shadow: 0 6px 24px rgba(0,0,0,0.12);
  }
  .brand-name {
    position: absolute;
    top: 62px; right: 52px;
    font-size: 28px; font-weight: 800;
    letter-spacing: 1px;
    color: var(--brand-blue);
  }
  .regulatory {
    position: absolute;
    left: 40px; top: 786px;
    font-size: 8px; line-height: 11px;
    color: var(--text-grey);
  }
  .regulatory .website { font-size: 9.5px; margin-bottom: 3px; color: var(--text-grey); }
  .regulatory .website strong { color: var(--brand-blue-light); font-weight: 800; }
  .company-contact {
    position: absolute;
    right: 40px; top: 836px;
    text-align: right;
    color: var(--text-grey);
    font-size: 9.5px;
  }
  .company-contact .company-name {
    font-size: 9px; font-weight: 800;
    color: var(--brand-blue);
    letter-spacing: 0.3px;
    margin-bottom: 5px;
  }
  .contact-line { display: flex; gap: 10px; justify-content: flex-end; align-items: center; }
  .phone { display: inline-flex; align-items: center; gap: 4px; }
  .phone svg { width: 10px; height: 10px; fill: var(--brand-blue); }
  .footer-band {
    position: absolute;
    left: 0; bottom: 0;
    width: 640px; height: 22px;
  }
</style>
</head>
<body>
  <main class="letterhead">
    <div class="brand-name">CORVANEL.COM</div>

    <div class="regulatory">
      <p class="website">www.<strong>corvanel</strong>.com.sg</p>
      <p>Licensed by the Treasury Conduct Bureau of Singapore</p>
      <p>QTLD licence no. XQZ908172-3</p>
    </div>

    <div class="company-contact">
      <p class="company-name">CORVANEL HOLDINGS PTE LTD</p>
      <p class="contact-line">
        <span>48 Harlow Street, #09-03 Meridian Tower, Singapore 058812</span>
        <span class="phone">
          <svg viewBox="0 0 24 24" aria-hidden="true"><path d="M6.6 10.8a15.1 15.1 0 0 0 6.6 6.6l2.2-2.2a1 1 0 0 1 1-.25 11.4 11.4 0 0 0 3.6.57 1 1 0 0 1 1 1V20a1 1 0 0 1-1 1A17 17 0 0 1 3 4a1 1 0 0 1 1-1h3.5a1 1 0 0 1 1 1c0 1.25.2 2.45.57 3.57a1 1 0 0 1-.25 1z"/></svg>
          +65 555 01847
        </span>
      </p>
    </div>

    <svg class="footer-band" viewBox="0 0 640 22" preserveAspectRatio="none" aria-hidden="true">
      <defs>
        <linearGradient id="bandBlue" x1="0" x2="1" y1="0" y2="0">
          <stop offset="0" stop-color="var(--brand-blue-light)"/>
          <stop offset="1" stop-color="var(--brand-blue-deep)"/>
        </linearGradient>
      </defs>
      <polygon points="0,0 196,0 182,22 0,22" fill="var(--band-grey)"/>
      <polygon points="212,0 640,0 640,22 198,22" fill="url(#bandBlue)"/>
    </svg>
  </main>
</body>
</html>
```